Kem7Dex Letterhead

Need a new letterhead for my law firm.
IDENTIFYING INFORMATION BELOW:
Ansel T Brightwater III
Attorney at Law
Address: 4832 Tillbury Rd, Ste 250, Dallas, TX 75204
Phone: 866-402-7183
Fax: 469-583-0271
Email: kem@kem7dex.example
Website: www.kem7dex.example

Colors
0054AA
0677BA
7BADD7
CADEEF
E8F1F8

Requirements
Must have
• Logo needs to be on the letterhead, along with identifying information which is included in the project description.

```html
<!DOCTYPE html>
<html lang="en">
<head>
<meta charset="utf-8">
<title>Kem7Dex Letterhead</title>
<link rel="stylesheet" href="https://fonts.googleapis.com/css2?family=Open+Sans:wght@400;600;700;800&display=swap">
<style>
  :root {
    --backdrop: #c4c4c4;
    --paper: #ffffff;
    --band-blue: #2ba9f1;
    --band-blue-deep: #1a8fdb;
    --accent: #0677ba;
    --shade: #e4e5ea;
    --ink: #111111;
    --body-ink: #6d6f73;
    --photo-dark: #1d1d1d;
    --photo-light: #d9d9d9;
  }
  * { margin: 0; padding: 0; box-sizing: border-box; }
  html, body { width: 1200px; height: 1200px; overflow: hidden; }
  body {
    background: var(--backdrop);
    font-family: "Open Sans", Arial, sans-serif;
    color: var(--ink);
  }
  .letterhead {
    position: absolute;
    left: 190px; top: 30px;
    width: 820px; height: 1140px;
    background: var(--paper);
    box-shadow: 0 10px 30px rgba(0,0,0,.18);
    overflow: hidden;
  }
  .decor { position: absolute; inset: 0; }
  .contact {
    position: absolute;
    font-size: 14px; line-height: 1.35; color: var(--ink);
    display: flex; align-items: center; gap: 10px;
  }
  .contact .icon { width: 18px; height: 18px; flex: none; }
  .contact-web { left: 330px; top: 42px; }
  .contact-phone { left: 590px; top: 42px; }
  .brand { position: absolute; left: 280px; top: 128px; text-align: center; }
  .brand-name {
    font-size: 56px; font-weight: 800; letter-spacing: 2px; line-height: 1;
    color: var(--ink);
  }
  .brand-tagline {
    font-size: 15px; letter-spacing: 5px; text-transform: uppercase;
    margin-top: 6px; color: var(--ink);
  }
  .date { position: absolute; right: 60px; top: 222px; font-size: 13px; }
  .date strong { font-weight: 600; }
  .recipient { position: absolute; left: 60px; top: 400px; font-size: 15px; line-height: 1.25; }
  .recipient .name { font-weight: 800; }
  .recipient-address { position: absolute; left: 80px; top: 480px; font-size: 15px; line-height: 1.25; }
  .letter-body {
    position: absolute; left: 300px; top: 262px; width: 470px;
    font-size: 12.5px; line-height: 2.05; color: var(--body-ink);
  }
  .letter-body .salutation { color: var(--ink); margin-bottom: 10px; }
  .letter-body p { margin-bottom: 16px; text-align: justify; }
  .signoff { position: absolute; left: 300px; top: 760px; font-size: 13px; color: var(--body-ink); }
  .signature-mark {
    position: absolute; left: 310px; top: 790px; width: 150px; height: 60px;
    background: linear-gradient(90deg, #ececec, #f7f7f7);
    border-radius: 4px;
  }
  .signer { position: absolute; left: 310px; top: 860px; }
  .signer-name { font-size: 24px; font-weight: 400; }
  .signer-title { font-size: 17px; font-weight: 800; }
  .portrait {
    position: absolute; left: 600px; top: 790px; width: 220px; height: 260px;
    background: linear-gradient(160deg, var(--photo-light) 0%, #8a8a8a 45%, var(--photo-dark) 100%);
  }
  .address {
    position: absolute; left: 60px; bottom: 40px;
    display: flex; align-items: center; gap: 12px; font-size: 15px;
  }
  .address .icon { width: 20px; height: 20px; }
</style>
</head>
<body>
  <main class="letterhead">
    <svg class="decor" width="820" height="1140" viewBox="0 0 820 1140" aria-hidden="true">
      <!-- header bands -->
      <polygon points="0,70 210,70 195,130 0,130" fill="var(--band-blue)"/>
      <polygon points="0,130 195,130 190,150 0,150" fill="var(--shade)"/>
      <polygon points="250,20 820,20 820,95 230,110 225,110" fill="var(--band-blue)"/>
      <polygon points="820,20 820,60 250,20" fill="var(--band-blue-deep)" opacity=".35"/>
      <!-- footer bands -->
      <line x1="330" y1="1040" x2="620" y2="1040" stroke="var(--ink)" stroke-width="5"/>
      <polygon points="370,1050 600,1050 585,1100 390,1100" fill="var(--band-blue)"/>
      <polygon points="390,1100 585,1100 580,1120 400,1120" fill="var(--shade)"/>
      <polygon points="610,1050 680,1050 670,1100 600,1100" fill="var(--band-blue)"/>
      <polygon points="600,1100 670,1100 665,1120 598,1120" fill="var(--shade)"/>
    </svg>

    <div class="contact contact-web">
      <svg class="icon" viewBox="0 0 18 18" aria-hidden="true"><circle cx="9" cy="9" r="9" fill="var(--ink)"/><rect x="4.5" y="6" width="9" height="6" fill="none" stroke="#fff" stroke-width="1"/><polyline points="4.5,6 9,9.5 13.5,6" fill="none" stroke="#fff" stroke-width="1"/></svg>
      <div>kem@kem7dex.example<br>www.kem7dex.example</div>
    </div>
    <div class="contact contact-phone">
      <svg class="icon" viewBox="0 0 18 18" aria-hidden="true"><circle cx="9" cy="9" r="9" fill="var(--ink)"/><path d="M6 5.5c.6-.4 1.1-.2 1.4.4l.6 1.2c.2.4 0 .8-.3 1l-.4.3c.4.9 1.1 1.6 2 2l.3-.4c.3-.3.7-.5 1-.3l1.2.6c.6.3.8.8.4 1.4-.6.9-1.6 1.2-2.6.7-1.9-.9-3.2-2.2-4.1-4.1-.5-1-.2-2 .5-2.8z" fill="#fff"/></svg>
      <div>866-402-7183<br>469-583-0271</div>
    </div>

    <div class="brand">
      <div class="brand-name">KEM7DEX</div>
      <div class="brand-tagline">Counsel you can count on</div>
    </div>

    <div class="date"><strong>Date:</strong> 15/01/2022</div>

    <div class="recipient">To<br><span class="name">Smith</span><br>Director</div>
    <div class="recipient-address">Address<br>Street name,<br>Avenue City</div>

    <section class="letter-body">
      <div class="salutation">Dear Sir,</div>
      <p>Lorem ipsum dolor sit amet, cons ectetuer adipiscing elit, sed diam nonummy nibh euismod tincidunt ut laoreet dolore magna aliquam erat volutpat. Ut wisi enim ad minim veniam, quis nostrud exerci tation ullamcorper suscipit lobortis nisl ut aliquip ex ea commodo consequat.</p>
      <p>Lorem ipsum dolor sit amet, consectetuer adipiscing elit, sed diam nonummy nibh euismod tincidunt ut laoreet dolore magna aliquam erat volutpat. Ut wisi enim ad minim veniam, quis nostrud exerci tation ullamcorper suscipit lobortis nisl ut aliquip ex ea commodo consequat. Duis autem vel eum iriure dolor in hendrerit in vulputate velit esse molestie consequat, vel illum dolore eu feugiat nulla facilisis at vero eros et accumsan et iusto odio dignissim qui blandit praesent luptatum zzril delenit augue duis dolore te feugait nulla facilisi.</p>
      <p>Lorem ipsum dolor sit amet, cons ectetuer adipiscing elit, sed diam nonummy nibh euismod tincidunt ut laoreet dolore magna aliquam erat volutpat. Ut wisi enim ad minim veniam.</p>
    </section>

    <div class="signoff">Regards,</div>
    <div class="signature-mark" role="img" aria-label="Handwritten signature of Ansel T Brightwater III"></div>
    <div class="signer">
      <div class="signer-name">Ansel T Brightwater III</div>
      <div class="signer-title">Attorney at Law</div>
    </div>

    <div class="portrait" role="img" aria-label="Black and white portrait photograph of the attorney"></div>

    <div class="address">
      <svg class="icon" viewBox="0 0 20 20" aria-hidden="true"><circle cx="10" cy="10" r="10" fill="var(--accent)"/><path d="M10 4.5a3.5 3.5 0 0 0-3.5 3.5c0 2.5 3.5 6.5 3.5 6.5s3.5-4 3.5-6.5A3.5 3.5 0 0 0 10 4.5z" fill="#fff"/><circle cx="10" cy="8" r="1.3" fill="var(--accent)"/></svg>
      <span>4832 Tillbury Rd, Ste 250, Dallas, TX 75204</span>
    </div>
  </main>
</body>
</html>
```